Webdesign für Ingenieurbüro
Zielgruppe
Ingenieurbüro Varnotek GmbH
Leistungen:
Siedlungswasserwirtschaft
Straßen- und Ingenieurbau
Hochwasserschutz / Wasserbau
Pegelanlagen
Komplexerschließungen
Koordinierung nach BaustellV
Landschaftsbau
Zielgruppe ist die Öffentliche Hand
Aufgabenstellung
Leistungsbereiche und Stellenangebote (zZt. 3 Stück) sollen zu gleichen Teilen im Fokus stehen. Call to action zum Berweberformular ist nötig.
Zu beachten wäre, dass das Unternehmen für öffentliche Auftraggeber arbeitet. Die Seite sollte klar strukturiert und seriös wirken.
Der Login-Bereich soll in den Hintergrund treten, eventuell über dem footer.
Logo aus dem Cover - siehe anbei übernehmen

```html
<!DOCTYPE html>
<html lang="de">
<head>
<meta charset="utf-8">
<title>Ingenieurbüro Varnotek GmbH</title>
<link href="https://fonts.googleapis.com/css2?family=Lato:wght@400;700;900&display=swap" rel="stylesheet">
<style>
:root{
  --navy:#0c3a8a;
  --navy-deep:#0b2d6a;
  --blue:#0a96db;
  --ink:#1d2a3a;
  --text:#2b2b2b;
  --pale:#eaf4fb;
  --white:#fff;
  --line:#d9dde3;
}
*{box-sizing:border-box;margin:0;padding:0}
html,body{width:1200px;height:2700px;overflow:hidden}
body{font-family:'Lato',sans-serif;color:var(--text);background:var(--white);position:relative}
.abs{position:absolute}

/* header */
.topbar{left:0;top:0;width:1200px;height:54px;background:var(--navy)}
.nav{right:120px;top:0;height:54px;display:flex;gap:44px;align-items:center;list-style:none}
.nav li{color:var(--white);font-size:14px}
.brand{left:118px;top:12px;width:212px;height:196px;border-radius:50%;background:var(--white);border:1px solid var(--blue);display:flex;flex-direction:column;align-items:center;justify-content:center;gap:10px;z-index:3}
.brand-dot{width:22px;height:22px;border-radius:50%;background:var(--navy)}
.brand-name{color:var(--navy);font-weight:700;font-size:17px;text-align:center;line-height:1.25}

/* hero */
.hero{left:0;top:54px;width:1200px;height:471px;background:linear-gradient(100deg,#eef7fd 0%,#d5ebf8 35%,#8fb6cc 60%,#5d7d86 85%,#4a5e55 100%)}
.hero-title{left:117px;top:316px;color:var(--navy);font-weight:900;font-size:38px;line-height:46px;letter-spacing:-.5px}
.hero-sub{left:120px;top:422px;width:470px;height:29px;background:var(--blue);color:var(--white);font-size:17px;padding:3px 11px}
.lead-form{left:956px;top:141px;width:244px;height:308px;background:var(--blue);padding:28px 21px 0 27px}
.lead-form h2{color:var(--white);font-size:15px;font-weight:700;line-height:18px;margin-bottom:16px}
.field{background:var(--white);height:28px;margin-bottom:6px;font-size:10px;color:#666;padding:8px 10px}
.field.tall{height:63px}
.btn-send{background:var(--navy);color:var(--white);height:28px;font-size:12px;text-align:center;line-height:28px;margin-top:2px}

/* welcome */
.welcome{left:0;top:525px;width:1200px;height:283px;background:var(--pale);border-bottom:1px solid var(--line)}
.welcome h2{position:absolute;left:120px;top:48px;color:var(--navy);font-weight:400;font-size:28px}
.welcome p{position:absolute;top:104px;width:325px;font-size:12.5px;line-height:22.6px}
.photo-frame{left:856px;top:572px;width:215px;height:178px;background:var(--white);padding:9px;transform:rotate(-5deg);box-shadow:0 3px 10px rgba(0,0,0,.25)}
.photo-frame div{width:100%;height:100%;background:linear-gradient(180deg,#a9c6e4 0%,#e8ecef 40%,#9aa3a8 80%,#6d6e6a 100%)}

/* services */
.section-title{width:1200px;text-align:center;color:var(--navy);font-weight:400;font-size:29px}
.card{width:210px;height:158px;background:var(--white);box-shadow:0 1px 6px rgba(0,0,0,.12);display:flex;flex-direction:column;align-items:center;padding-top:30px}
.card svg{height:56px}
.card .rule{width:160px;height:1px;background:var(--line);margin-top:12px}
.card span{font-size:13px;line-height:16px;text-align:center;margin-top:8px;color:#333}
.card.active{background:var(--blue)}
.card.active span{color:var(--white);font-weight:700}
.card.active .rule{background:rgba(255,255,255,.4)}

/* jobs */
.jobs-photo{left:0;top:1348px;width:599px;height:362px;background:linear-gradient(160deg,#6d5a52 0%,#c9997a 30%,#7d7278 60%,#2f3647 100%)}
.jobs{left:599px;top:1348px;width:601px;height:362px;background:var(--blue);color:var(--white);padding:72px 44px}
.jobs h2{font-size:20px;font-weight:700}
.jobs .intro{font-size:12px;font-weight:700;margin-top:24px}
.jobs ul{list-style:none;margin-top:22px}
.jobs li{font-size:12.5px;line-height:22.5px}
.chev{display:inline-block;margin-right:9px;font-size:11px}
.btn-apply{display:inline-block;margin-top:26px;border:1.5px solid var(--white);width:153px;height:36px;text-align:center;line-height:33px;font-size:12.5px;font-weight:700}

/* projects */
.project{width:301px;height:205px}
.project .img{height:175px}
.project .cap{height:30px;background:var(--navy);color:var(--white);font-weight:700;font-size:13px;line-height:30px;padding-left:12px}

/* news */
.news{left:0;top:2087px;width:1200px;height:361px;background:var(--pale);border-top:1px solid var(--line)}
.news-nav{display:flex;gap:2px}
.news-nav div{width:27px;height:30px;background:var(--navy);color:var(--white);text-align:center;line-height:30px;font-size:13px}
.news-frame{left:120px;top:2163px;width:435px;height:255px;background:var(--white);padding:8px;box-shadow:0 1px 5px rgba(0,0,0,.15)}
.news-frame div{width:100%;height:100%;background:linear-gradient(180deg,#5a86bf 0%,#9fb6c9 30%,#cfc0a3 55%,#7f8c6a 85%,#4f6a3a 100%)}
.news-text{left:592px;top:2236px;width:400px;font-size:11px;line-height:18px;color:#222}
.news-text .date{color:var(--navy);font-weight:700;margin-bottom:16px}
.news-text .more{color:var(--navy);font-weight:700;text-decoration:underline;margin-top:16px}

/* login */
.login{left:0;top:2448px;width:1200px;height:120px;background:linear-gradient(90deg,#1259b4 0%,#0a7fd0 60%,#0a9ae0 100%)}
.login h2{position:absolute;left:336px;top:20px;color:var(--white);font-size:18px;font-weight:700}
.login .input{position:absolute;top:47px;width:265px;height:36px;background:var(--white);font-size:12px;line-height:36px;padding-left:12px;color:#333}
.login .btn{position:absolute;left:902px;top:47px;width:177px;height:36px;background:var(--navy);color:var(--white);font-size:13px;font-weight:700;text-align:center;line-height:36px}
.login .forgot{position:absolute;right:121px;top:93px;color:var(--white);font-size:11px;font-weight:700}

/* footer */
.footer{left:0;top:2568px;width:1200px;height:132px;background:var(--navy-deep);color:var(--white)}
.footer .addr{position:absolute;left:120px;top:43px;font-size:10px;line-height:18px}
.footer .addr b{font-size:12.5px}
.footer .mark{position:absolute;left:520px;top:28px;width:160px;text-align:center;font-size:12px;font-weight:700;display:flex;flex-direction:column;align-items:center;gap:6px}
.footer .mark i{width:14px;height:14px;border-radius:50%;background:var(--white)}
.footer .contact{position:absolute;left:908px;top:40px;font-size:10px;line-height:18px}
</style>
</head>
<body>

<header>
  <div class="abs topbar"></div>
  <ul class="abs nav">
    <li>Home</li><li>Stellenangebote</li><li>Leistungen</li><li>Unternehmen</li><li>Projekte</li><li>Kontakt</li>
  </ul>
  <div class="abs brand">
    <div class="brand-dot"></div>
    <div class="brand-name">Ingenieurbüro<br>Varnotek GmbH</div>
  </div>
</header>

<section>
  <div class="abs hero" role="img" aria-label="Foto eines Flusslaufs mit Steinufer und Gebäuden im Hintergrund"></div>
  <h1 class="abs hero-title">Über 25 Jahre Ingenieurbüro<br>Varnotek GmbH</h1>
  <div class="abs hero-sub">Ingenieurleistungen aus Weißbach-Talheim seit 1991</div>
  <form class="abs lead-form">
    <h2>Excepteur sint occaecat cupidatat non proident</h2>
    <div class="field">Name</div>
    <div class="field">Email</div>
    <div class="field">Telefon</div>
    <div class="field tall">Kommentare</div>
    <div class="btn-send">SENDEN</div>
  </form>
</section>

<section class="abs welcome">
  <h2>Herzlich willkommen</h2>
  <p style="left:120px">Willkommen bei der Ingenieurbüro VARNOTEK GmbH, einem mittelständischen Unternehmen, welches 1991 gegründet wurde. Wir sind ein zuverlässiger Partner für fachgerechte Beratung, Planung und Bauüberwachung von Maßnahmen des Tief-, Wasser- und Straßenbaues.</p>
  <p style="left:507px">Hierfür sind 18 hochqualifizierte und engagierte Ing-enieure und technische Mitarbeiter verantwortlich. Mod-ernste Kommunikationstechnik und Spezialsoftware, sowie die Kreativität der Mitarbeiter sind ein Garant für effektive Lösungen.</p>
</section>
<div class="abs photo-frame"><div role="img" aria-label="Foto des Bürogebäudes mit parkenden Autos"></div></div>

<section>
  <h2 class="abs section-title" style="left:0;top:858px">Leistungen</h2>
  <div class="abs card" style="left:120px;top:930px">
    <svg viewBox="0 0 56 56" fill="none" stroke="#0a96db" stroke-width="2"><path d="M24 6c-8 12-14 20-14 28a14 14 0 0 0 14 14"/><circle cx="32" cy="30" r="9"/><circle cx="32" cy="30" r="3"/></svg>
    <div class="rule"></div><span>Siedlungswasser-<br>wirtschaft</span>
  </div>
  <div class="abs card active" style="left:369px;top:930px">
    <svg viewBox="0 0 66 66" fill="none"><circle cx="33" cy="33" r="33" fill="rgba(255,255,255,.25)"/><path d="M18 34a15 15 0 0 1 30 0M15 34h36M24 38c0 8 18 8 18 0" stroke="#fff" stroke-width="2"/></svg>
    <div class="rule"></div><span>Straßen- und<br>Ingenieurbau</span>
  </div>
  <div class="abs card" style="left:619px;top:930px">
    <svg viewBox="0 0 56 56" fill="none" stroke="#0a96db" stroke-width="2"><path d="M8 28L26 12l18 16M12 26v14h28V26"/><rect x="22" y="30" width="8" height="10"/><path d="M6 46c6-4 10 4 16 0s10 4 16 0 10 4 12 0"/></svg>
    <div class="rule"></div><span>Hochwasserschutz /<br>Wasserbau</span>
  </div>
  <div class="abs card" style="left:869px;top:930px">
    <svg viewBox="0 0 56 56" fill="none"><path d="M10 44a20 20 0 1 1 36 0" stroke="#0c3a8a" stroke-width="7"/><path d="M28 36l8-14" stroke="#0a96db" stroke-width="4"/></svg>
    <div class="rule"></div><span>Pegelanlagen</span>
  </div>
  <div class="abs card" style="left:369px;top:1126px">
    <svg viewBox="0 0 56 56" fill="none" stroke="#0a96db" stroke-width="2"><rect x="8" y="6" width="40" height="40"/><path d="M8 6l40 40M48 6L8 46M28 6v40M8 26h40"/><path d="M4 50h48"/></svg>
    <div class="rule" style="background:transparent"></div><span>Komplexerschließungen</span>
  </div>
  <div class="abs card" style="left:619px;top:1126px">
    <svg viewBox="0 0 56 56" fill="none" stroke="#0a96db" stroke-width="2"><circle cx="10" cy="10" r="5"/><rect x="40" y="4" width="12" height="12"/><circle cx="46" cy="44" r="5"/><rect x="4" y="38" width="12" height="10"/><path d="M20 46c0-10 16-10 16 0M22 22h12"/></svg>
    <div class="rule" style="background:transparent"></div><span>Koordinierung nach<br>BaustellV</span>
  </div>
</section>

<section>
  <div class="abs jobs-photo" role="img" aria-label="Foto eines gelben Schutzhelms auf Solarmodulen im Abendlicht"></div>
  <div class="abs jobs">
    <h2>Stellenangebote</h2>
    <p class="intro">Wir haben aktuell Stellenangebote aus den folgenden Bereichen:</p>
    <ul>
      <li><span class="chev">&gt;</span>Hydrologie</li>
      <li><span class="chev">&gt;</span>Wasserwirtschaft</li>
      <li><span class="chev">&gt;</span>Verkehrsanlagen</li>
    </ul>
    <div class="btn-apply"><span class="chev">&gt;</span>Jetzt bewerben</div>
  </div>
</section>

<section>
  <h2 class="abs section-title" style="left:0;top:1756px">Projekte</h2>
  <svg class="abs" style="left:72px;top:1903px" width="24" height="36" viewBox="0 0 24 36" fill="none" stroke="#0a96db" stroke-width="2.5"><path d="M20 2L4 18l16 16"/></svg>
  <svg class="abs" style="left:1104px;top:1903px" width="24" height="36" viewBox="0 0 24 36" fill="none" stroke="#0a96db" stroke-width="2.5"><path d="M4 2l16 16L4 34"/></svg>
  <div class="abs project" style="left:120px;top:1823px">
    <div class="img" role="img" aria-label="Foto einer Baustelle mit Bauzaun vor Wohnhäusern" style="background:linear-gradient(180deg,#c9d4dc 0%,#6f7a62 50%,#58564f 100%)"></div>
    <div class="cap"><span class="chev">&gt;</span>Siedlungswasserwirtschaft</div>
  </div>
  <div class="abs project" style="left:450px;top:1823px">
    <div class="img" role="img" aria-label="Foto von Asphaltarbeiten auf einer Straße" style="background:linear-gradient(180deg,#d8e0e6 0%,#6c7c60 45%,#4a4c50 100%)"></div>
    <div class="cap"><span class="chev">&gt;</span>Straßen- und Ingenieurbau</div>
  </div>
  <div class="abs project" style="left:779px;top:1823px">
    <div class="img" role="img" aria-label="Foto eines begrünten Hochwasserdeichs" style="background:linear-gradient(180deg,#c6d6e6 0%,#9cb2c6 35%,#5f8040 60%,#3f6428 100%)"></div>
    <div class="cap"><span class="chev">&gt;</span>Hochwasserschutz / Wasserbau</div>
  </div>
</section>

<section class="abs news">
  <h2 class="section-title" style="position:absolute;left:0;top:28px">News</h2>
  <div class="news-nav" style="position:absolute;left:1024px;top:38px"><div>&lt;</div><div>&gt;</div></div>
</section>
<div class="abs news-frame"><div role="img" aria-label="Foto einer Wehranlage mit Stahlkonstruktion"></div></div>
<div class="abs news-text">
  <p class="date">17.05.-21.05.2010</p>
  <p>Qualifizierung zum Sicherheits- und Gesundheitsschutz-Koordinator gemäß<br>Anlagen B &amp; C zur RAB 30 in Neuss</p>
  <p class="more">Mehr</p>
</div>

<section class="abs login">
  <svg style="position:absolute;left:122px;top:16px" width="106" height="92" viewBox="0 0 106 92" fill="none" stroke="rgba(255,255,255,.75)" stroke-width="2.5"><circle cx="24" cy="22" r="19"/><path d="M2 88V66a20 20 0 0 1 40-6v28z"/><rect x="52" y="44" width="44" height="36" rx="4" transform="rotate(-15 74 62)"/><path d="M60 42v-10a14 14 0 0 1 28 0v6"/><circle cx="76" cy="62" r="4"/></svg>
  <h2>Interner Bereich</h2>
  <div class="input" style="left:336px">Kundennummer</div>
  <div class="input" style="left:620px">Passwort</div>
  <div class="btn">LOGIN</div>
  <div class="forgot">Passwort vergessen?</div>
</section>

<footer class="abs footer">
  <div class="addr"><b>Ingenieurbüro Varnotek GmbH</b><br>Auenweg 214<br>09231 Weißbach</div>
  <div class="mark"><i></i>Ingenieurbüro<br>Varnotek GmbH</div>
  <div class="contact">Tel.&nbsp;&nbsp; 0375 / 44820-0<br>Fax:&nbsp;&nbsp; 0375 / 44820-19<br>Email : ingenieurbuero@varnotek.de</div>
</footer>

</body>
</html>
```